Plumvale CEO needs a Crowdsourced Graphic for a Wirelark Article

I need a simple graphic / banner for a blog post that's going to be posted on Wirelark (www.wirelark.com) - the biggest tech blog in the world.

The article will be written by Tobin Marsh (Plumvale's CEO) and the title will be "Asia's Secret Crowdsourcing Boom". The article is about the tens of thousands of people using crowdsourcing websites (like Plumvale.com, Qorvel.com and Vantrio.com) in China, India, the Philippines, Australia and other countries in the Asia Pacific region.

We'd really like to get this ASAP - so early submissions encouraged. We will try and get the winning designer linked to from the article.

Thanks to everyone that submitted!  Some great designs and hard to choose! :)

Target Market(s)

Tech saavy readers, English speakers

Industry/Entity Type

Tech

Requirements
Must have
• The graphic SHOULD:
1) Have the text "Asia's secret crowdsourcing boom" with some nice design and fonts (consider grey subtle pattern background and white drop shadow on fonts) - see attached examples
2) Have an Asian theme
3) Have the dimensions 640px wide by 240px wide
Nice to have
• The graphic COULD:
1) Have references to some or all of the countries mentioned above or use Asian characters as part of the background / motif (maybe the word "crowd" or "crowd sourcing" in different languages). In Chinese, the word for crowdsourcing is "witkey" (and there are corresponding Chinese characters: ??)
2) Emphasize the word "Asia" (using color and larger/different font)
3) Use a chart showing exponential (i.e. fast) growth - like the attached
4) Have a second line of text "5 Things You Didn't Know About Crowdsourcing in Asia"

```html
<!DOCTYPE html>
<html lang="en">
<head>
<meta charset="utf-8">
<title>Asia's Secret Crowdsourcing Boom</title>
<link rel="stylesheet" href="https://fonts.googleapis.com/css2?family=Archivo+Black&family=Russo+One&family=Oswald:wght@500;700&display=swap">
<style>
  :root {
    --bg-deep: #0b1622;
    --bg-mid: #1c3347;
    --bg-glow: #2d4b63;
    --ink-white: #ffffff;
    --asia-top: #ffd23a;
    --asia-bottom: #f27a12;
    --title-stroke: #8fa6b8;
    --ghost-word: rgba(150, 180, 200, 0.16);
    --tab-light: #e6fbff;
    --tab-mid: #8fe3f3;
    --tab-edge: #3fc2de;
    --tab-ink: #1a2a36;
    --trace: rgba(140, 220, 240, 0.35);
  }
  * { margin: 0; padding: 0; box-sizing: border-box; }
  html, body { width: 1200px; height: 450px; overflow: hidden; background: var(--bg-deep); }

  .banner {
    position: relative;
    width: 1200px;
    height: 450px;
    overflow: hidden;
    background: radial-gradient(ellipse 70% 80% at 50% 20%, var(--bg-glow) 0%, var(--bg-mid) 45%, var(--bg-deep) 100%);
  }

  .ghost-words span {
    position: absolute;
    font-family: "Oswald", sans-serif;
    font-weight: 700;
    color: var(--ghost-word);
    white-space: nowrap;
  }

  .circuit { position: absolute; inset: 0; }

  .headline { position: absolute; inset: 0; font-size: 0; }

  .headline-asia {
    position: absolute;
    left: 44px;
    top: 40px;
    font-family: "Archivo Black", sans-serif;
    font-size: 112px;
    line-height: 1;
    white-space: nowrap;
    color: var(--asia-bottom);
    background: linear-gradient(180deg, var(--asia-top) 20%, var(--asia-bottom) 80%);
    -webkit-background-clip: text;
    background-clip: text;
    -webkit-text-fill-color: transparent;
    -webkit-text-stroke: 3px var(--ink-white);
    paint-order: stroke fill;
    filter: drop-shadow(0 0 8px rgba(255,255,255,0.45));
  }
  .headline-asia .small-caps { font-size: 80px; }
  .headline-asia .apos { font-size: 80px; -webkit-text-fill-color: var(--ink-white); }

  .headline-rest-art { position: absolute; left: 0; top: 0; overflow: visible; }
  .headline-rest {
    font-family: "Russo One", sans-serif;
    font-size: 58px;
    fill: var(--ink-white);
    stroke: var(--title-stroke);
    stroke-width: 4px;
    paint-order: stroke fill;
    filter: drop-shadow(0 0 8px rgba(255,255,255,0.55));
  }

  .subtitle {
    position: absolute;
    left: 244px;
    top: 184px;
    font-family: "Oswald", sans-serif;
    font-weight: 500;
    font-size: 33px;
    line-height: 1;
    color: var(--ink-white);
    text-shadow: 0 0 8px rgba(255,255,255,0.45);
    white-space: nowrap;
  }

  .byline-tab {
    position: absolute;
    right: -10px;
    top: 366px;
    width: 376px;
    height: 72px;
    border-radius: 26px 0 0 26px;
    background: linear-gradient(180deg, var(--tab-light) 0%, var(--tab-mid) 70%, var(--tab-edge) 100%);
    border: 3px solid var(--tab-edge);
    box-shadow: 0 0 14px rgba(90, 210, 240, 0.55);
    transform: skewX(-18deg);
    transform-origin: bottom left;
  }
  .byline {
    position: absolute;
    right: 22px;
    top: 396px;
    font-family: "Oswald", sans-serif;
    font-weight: 500;
    font-size: 24px;
    line-height: 1;
    color: var(--tab-ink);
    white-space: nowrap;
  }
</style>
</head>
<body>
<main class="banner">
  <div class="ghost-words" aria-hidden="true">
    <span style="left:60px;top:240px;font-size:22px;transform:rotate(-15deg)">CrowdSourcing</span>
    <span style="left:190px;top:262px;font-size:28px;transform:rotate(8deg)">CrowdSourcing</span>
    <span style="left:40px;top:315px;font-size:24px;transform:rotate(-6deg)">CrowdSourcing</span>
    <span style="left:250px;top:345px;font-size:26px;transform:rotate(18deg)">CrowdSourcing</span>
    <span style="left:560px;top:250px;font-size:30px;transform:rotate(-10deg)">CrowdSourcing</span>
    <span style="left:620px;top:330px;font-size:22px;transform:rotate(12deg)">CrowdSourcing</span>
    <span style="left:880px;top:240px;font-size:26px;transform:rotate(20deg)">CrowdSourcing</span>
    <span style="left:1000px;top:20px;font-size:24px;transform:rotate(14deg)">CrowdSourcing</span>
    <span style="left:980px;top:290px;font-size:28px;transform:rotate(-12deg)">CrowdSourcing</span>
    <span style="left:400px;top:382px;font-size:22px;transform:rotate(-4deg)">CrowdSourcing</span>
  </div>

  <svg class="circuit" width="1200" height="450" viewBox="0 0 1200 450" aria-hidden="true">
    <path d="M0 290 H40 Q70 290 70 320 V376 Q70 416 110 416 H825" fill="none" stroke="var(--trace)" stroke-width="3"/>
    <path d="M0 308 H28 Q52 308 52 332 V384 Q52 432 100 432 H825" fill="none" stroke="var(--trace)" stroke-width="1.5" opacity="0.6"/>
  </svg>

  <h1 class="headline" aria-label="Asia's Secret Crowdsourcing Boom">
    <span class="headline-asia" aria-hidden="true">A<span class="small-caps">SIA</span><span class="apos">'s</span></span>
    <svg class="headline-rest-art" width="1200" height="200" viewBox="0 0 1200 200" aria-hidden="true">
      <text class="headline-rest" x="358" y="146" textLength="776" lengthAdjust="spacingAndGlyphs">SECRET CROWDSOURCING BOOM</text>
    </svg>
  </h1>
  <p class="subtitle">5 Things You Didn't Know About Crowdsourcing in Asia</p>

  <div class="byline-tab" aria-hidden="true"></div>
  <p class="byline">written by Tobin Marsh</p>
</main>
</body>
</html>
```